ink nest studio nos proporciona ter várias ideias vindo de mentes criativas diferentes o que nos faz termos muito mais variedades do que se uma única pessoa criasse vários logos.

```html
<!DOCTYPE html>
<html lang="pt">
<head>
<meta charset="utf-8">
<title>Rolo Produções — Pasta</title>
<link rel="stylesheet" href="https://fonts.googleapis.com/css2?family=Montserrat:wght@400;600;700&display=swap">
<style>
  :root {
    --bg: #9fb3b2;
    --paper: #f4f4f4;
    --ink: #4a4a4a;
    --cyan: #2aa8e0;
    --purple: #b748c4;
    --yellow: #f2e316;
    --pink: #ee2a62;
    --green: #3ccf3c;
  }
  * { box-sizing: border-box; margin: 0; padding: 0; }
  html, body { width: 1200px; height: 1200px; overflow: hidden; }
  body {
    background: var(--bg);
    font-family: "Montserrat", sans-serif;
    display: flex;
    align-items: center;
    justify-content: center;
  }
  .folder-spread {
    display: flex;
    width: 920px;
    height: 650px;
    box-shadow: 0 18px 40px rgba(0,0,0,0.18);
  }
  .panel {
    position: relative;
    width: 460px;
    height: 100%;
    background: var(--paper);
    display: flex;
    flex-direction: column;
    justify-content: space-between;
  }
  .panel--back { border-right: 1px solid #e2e2e2; }
  .band { display: flex; height: 44px; }
  .band span { display: block; height: 100%; }
  .c-cyan { background: var(--cyan); }
  .c-purple { background: var(--purple); }
  .c-yellow { background: var(--yellow); }
  .c-pink { background: var(--pink); }
  .c-green { background: var(--green); }

  .brand {
    position: absolute;
    left: 50%;
    top: 50%;
    transform: translate(-50%, -50%);
    display: flex;
    align-items: center;
    gap: 10px;
    color: var(--ink);
    font-weight: 700;
    white-space: nowrap;
  }
  .brand__mark { display: block; background: var(--cyan); border-radius: 50%; }
  .brand--front { top: 40%; font-size: 30px; letter-spacing: 0.5px; }
  .brand--front .brand__mark { width: 34px; height: 34px; }
  .brand--back { top: 46%; font-size: 11px; gap: 6px; }
  .brand--back .brand__mark { width: 12px; height: 12px; }

  .contact-list {
    position: absolute;
    left: 16px;
    bottom: 58px;
    list-style: none;
    font-size: 8px;
    color: var(--ink);
    line-height: 1;
  }
  .contact-list li { display: flex; align-items: center; gap: 6px; margin-top: 5px; }
  .contact-list svg { width: 9px; height: 9px; flex: none; }
</style>
</head>
<body>
  <main class="folder-spread">
    <section class="panel panel--back">
      <div class="band">
        <span class="c-cyan" style="width:12%"></span>
        <span class="c-purple" style="width:33%"></span>
        <span class="c-yellow" style="width:30%"></span>
        <span class="c-pink" style="width:25%"></span>
      </div>
      <div class="brand brand--back">
        <span class="brand__mark"></span>
        <span class="brand__name">ROLO PRODUÇÕES</span>
      </div>
      <ul class="contact-list">
        <li>
          <svg viewBox="0 0 10 10"><circle cx="5" cy="5" r="5" fill="var(--cyan)"/></svg>
          Rua das Flores 120, Lisboa
        </li>
        <li>
          <svg viewBox="0 0 10 10"><circle cx="5" cy="5" r="5" fill="var(--green)"/></svg>
          contato@roloproducoes.pt
        </li>
        <li>
          <svg viewBox="0 0 10 10"><circle cx="5" cy="5" r="5" fill="var(--pink)"/></svg>
          +351 210 000 000
        </li>
        <li>
          <svg viewBox="0 0 10 10"><circle cx="5" cy="5" r="5" fill="var(--purple)"/></svg>
          www.roloproducoes.pt
        </li>
      </ul>
      <div class="band">
        <span class="c-cyan" style="width:12%"></span>
        <span class="c-green" style="width:33%"></span>
        <span class="c-pink" style="width:30%"></span>
        <span class="c-yellow" style="width:25%"></span>
      </div>
    </section>

    <section class="panel panel--front">
      <div class="band">
        <span class="c-pink" style="width:32%"></span>
        <span class="c-green" style="width:40%"></span>
        <span class="c-cyan" style="width:28%"></span>
      </div>
      <div class="brand brand--front">
        <span class="brand__mark"></span>
        <span class="brand__name">ROLO PRODUÇÕES</span>
      </div>
      <div class="band">
        <span class="c-yellow" style="width:36%"></span>
        <span class="c-purple" style="width:40%"></span>
        <span class="c-cyan" style="width:24%"></span>
      </div>
    </section>
  </main>
</body>
</html>
```